Full service meeting planning company needs new business cards

Velmora Linkway is a full service meeting planning company that specializes in on-line conference registration web development and event communications. We combine citywide hotel management, mobile applications, eblast reminders, confirmation letters, and customized reporting to create a seamless registration process. We also manage group motor coach transportation, food and beverages, entertainment, stage and lighting for group of 10 to 4000.

Target Market(s)

Corporations and associations

Industry/Entity Type

Event Planning

Contact Information for Business Card

standard size 3.5" wide and 2" tall

Font styles to use
Serif
Sans Serif

Colors
f37122
f78f20
333333
5c5c5c
9d9d9d
f68d4d

Requirements
Must have
• {name}
• Velmora Linkway
• P.O. Box 7384, Grand Rapids, M I 49568
• www.velmoralinkway.com
• {email}
• {phone}
• {mobile phone}
Nice to have
• Our colors are black, grey and orange as an accent color
Should not have
• I am not happy with our website layout anymore either. It feels dark and old but it does explain who we are pretty well if you'd like to review; www.velmoralinkway.com

```html
<!DOCTYPE html>
<html lang="en">
<head>
<meta charset="utf-8">
<title>Velmora Linkway – Business Cards</title>
<link href="https://fonts.googleapis.com/css2?family=Lato:wght@400;700&display=swap" rel="stylesheet">
<style>
  :root {
    --orange: #f08524;
    --orange-deep: #f37122;
    --ink: #333333;
    --ink-soft: #3d3d3d;
    --card: #ffffff;
    --backdrop: #e8e5e2;
  }
  * { margin: 0; padding: 0; box-sizing: border-box; }
  html, body {
    width: 1200px; height: 900px; overflow: hidden;
    background: var(--backdrop);
    font-family: "Lato", Arial, sans-serif;
  }
  .canvas { position: relative; width: 1200px; height: 900px; }

  /* Front card */
  .card-front {
    position: absolute; left: 238px; top: 62px;
    width: 554px; height: 343px;
    background: var(--card); overflow: hidden;
    box-shadow: 0 6px 18px rgba(0,0,0,.15);
  }
  .front-disc {
    position: absolute; left: 211px; top: -2px;
    width: 344px; height: 344px; border-radius: 50%;
    background: var(--orange);
    display: flex; align-items: center; justify-content: center;
  }
  .front-disc .brand-name {
    color: var(--card); font-weight: 700; font-size: 30px;
    letter-spacing: 1px; text-align: center; line-height: 1.25;
    text-transform: uppercase;
  }
  .person-name {
    position: absolute; left: 33px; top: 48px;
    color: var(--orange); font-weight: 700; font-size: 18.5px;
  }
  .person-title {
    position: absolute; left: 33px; top: 71px;
    color: var(--ink); font-size: 15px;
  }
  .address {
    position: absolute; left: 33px; top: 136px;
    color: var(--ink); font-size: 15px; line-height: 20px;
  }
  .contacts {
    position: absolute; left: 33px; top: 220px;
    list-style: none; color: var(--ink); font-size: 15px;
  }
  .contacts li { display: flex; align-items: center; height: 20px; }
  .contacts svg { width: 11px; height: 11px; margin-right: 10px; fill: var(--orange); }

  /* Back card */
  .card-back {
    position: absolute; left: 458px; top: 518px;
    width: 560px; height: 342px;
    background: var(--card);
    border-radius: 171px 0 0 171px;
    box-shadow: 0 6px 18px rgba(0,0,0,.15);
  }
  .back-mark {
    position: absolute; left: 355px; top: 163px;
    width: 114px; height: 114px; border-radius: 50%;
    background: var(--orange);
  }
  .back-name {
    position: absolute; left: 295px; top: 290px;
    color: var(--orange); font-weight: 700; font-size: 21px;
    letter-spacing: .3px; white-space: nowrap; text-transform: uppercase;
  }
</style>
</head>
<body>
<main class="canvas">
  <section class="card-front" aria-label="Business card front">
    <h1 class="person-name">Daniel Harper</h1>
    <p class="person-title">Managing Director</p>
    <address class="address">P.O. Box 7384,<br>Grand Rapids<br>M I 49568</address>
    <ul class="contacts">
      <li><svg viewBox="0 0 12 12"><rect x="3" y="0" width="6" height="12" rx="1.2"/></svg>555 018 274</li>
      <li><svg viewBox="0 0 12 12"><path d="M2.4 0.5 4.6 3 3.5 4.4a7 7 0 0 0 4.1 4.1L9 7.4l2.5 2.2-1.3 1.9C5.4 11.4 0.6 6.6 0.5 1.8Z"/></svg>044-555 018 274</li>
      <li><svg viewBox="0 0 12 12"><path d="M0 2h12v1.2L6 7 0 3.2Z M0 4.6 6 8.4 12 4.6V10H0Z"/></svg>info@velmoralinkway.com</li>
      <li><svg viewBox="0 0 12 12"><circle cx="6" cy="6" r="6"/></svg>www.velmoralinkway.com</li>
    </ul>
    <div class="front-disc"><span class="brand-name">Velmora<br>Linkway</span></div>
  </section>

  <section class="card-back" aria-label="Business card back">
    <div class="back-mark"></div>
    <p class="back-name">Velmora Linkway</p>
  </section>
</main>
</body>
</html>
```